Business Cards for Live Events Company

We are Flumo's.
We are Looking for a business card design for our live entertainment technical company.
We design lighting, video, and audio for Theatre, Live events, and Concerts.

We also hire out technical equipment for these, which includes: Lights, Special FX, Audio, Video, Projection, LED Screens, Rigging, Staging.

Have a look at our website and Facebook page for an idea of what we do.
www.flumos.com.au www.facebook.com/flumosproductions

Be creative with the design, we are looking for something eye catching.

included are 4 different styles of our logo which we use. Take your pick of what you prefer.

Industry/Entity Type

Events

Font styles to use
Serif
Sans Serif
Script

Requirements
Must have
• Eye catching, we are a design company creative events.
all the usual contact details etc.
Nice to have
• good use of colour
Should not have
• Nothing really....

```html
<!DOCTYPE html>
<html lang="en">
<head>
<meta charset="utf-8">
<title>Flumo's – Business Cards</title>
<link rel="stylesheet" href="https://fonts.googleapis.com/css2?family=Jost:wght@400;600&display=swap">
<style>
  :root {
    --page: #ffffff;
    --card: #131313;
    --band: #191919;
    --rule: #2c2c2c;
    --pattern-light: #2a2a2a;
    --pattern-mid: #1f1f1f;
    --logo: #c6c6c6;
    --text: #c0c0c0;
    --teal: #2bb3b1;
    --cyan: #2aa7de;
    --purple: #8259c0;
  }
  * { margin: 0; padding: 0; box-sizing: border-box; }
  html, body {
    width: 1200px; height: 927px; overflow: hidden;
    background: var(--page);
    font-family: "Jost", "Century Gothic", sans-serif;
  }
  .sheet { position: relative; width: 1200px; height: 927px; }
  .card {
    position: absolute; top: 296px;
    width: 586px; height: 335px;
    background: var(--card); overflow: hidden;
  }
  .card--front { left: 8px; }
  .card--back { left: 606px; }

  /* background lettering areas, filled in their main tones */
  .pattern-zone { position: absolute; left: 0; width: 100%; }
  .pattern-zone--top {
    top: 0; height: 115px;
    background:
      radial-gradient(ellipse 30% 90% at 12% 40%, var(--pattern-light), transparent 70%),
      radial-gradient(ellipse 22% 100% at 36% 60%, var(--pattern-light), transparent 70%),
      radial-gradient(ellipse 22% 100% at 68% 40%, var(--pattern-light), transparent 70%),
      radial-gradient(ellipse 22% 90% at 92% 60%, var(--pattern-light), transparent 70%),
      var(--pattern-mid);
  }
  .pattern-zone--bottom {
    bottom: 0; height: 112px;
    background:
      radial-gradient(ellipse 22% 100% at 18% 60%, var(--pattern-light), transparent 70%),
      radial-gradient(ellipse 16% 100% at 44% 55%, var(--pattern-light), transparent 70%),
      radial-gradient(ellipse 22% 100% at 62% 60%, var(--pattern-light), transparent 70%),
      radial-gradient(ellipse 22% 100% at 92% 50%, var(--pattern-light), transparent 70%),
      var(--pattern-mid);
  }
  .brand-band {
    position: absolute; left: 0; top: 115px; width: 100%; height: 108px;
    background: var(--band);
    border-top: 3px solid var(--rule); border-bottom: 3px solid var(--rule);
  }
  .brand { position: absolute; left: 40px; top: 6px; }
  .brand__name {
    color: var(--logo); font-size: 66px; font-weight: 400;
    line-height: 1; letter-spacing: -0.5px;
  }
  .brand__tagline {
    color: var(--logo); font-size: 13px; letter-spacing: 0.8px;
    margin-top: 3px; white-space: nowrap;
  }
  .social { position: absolute; left: 397px; top: 8px; list-style: none; }
  .social li {
    display: flex; align-items: center; gap: 7px;
    height: 29.5px; font-size: 15px; letter-spacing: -0.3px; white-space: nowrap;
  }
  .social .mark { width: 21px; height: 21px; flex: none; background: currentColor; border-radius: 4px; }
  .social .mark--round { border-radius: 50%; }
  .teal { color: var(--teal); }
  .cyan { color: var(--cyan); }
  .purple { color: var(--purple); }

  /* back */
  .pattern-column {
    position: absolute; left: 0; top: 0; width: 190px; height: 100%;
    background:
      radial-gradient(ellipse 70% 22% at 40% 12%, var(--pattern-light), transparent 70%),
      radial-gradient(ellipse 60% 20% at 55% 38%, var(--pattern-light), transparent 70%),
      radial-gradient(ellipse 70% 20% at 45% 64%, var(--pattern-light), transparent 70%),
      radial-gradient(ellipse 60% 22% at 40% 90%, var(--pattern-light), transparent 70%),
      var(--pattern-mid);
    border-right: 5px solid var(--rule);
  }
  .back-head {
    position: absolute; left: 195px; top: 0; right: 0; height: 68px;
    border-bottom: 3px solid var(--rule);
  }
  .back-head .brand__name { position: absolute; left: 23px; top: 14px; font-size: 50px; }
  .back-tagline {
    position: absolute; left: 218px; top: 71px;
    color: var(--text); font-size: 14.5px; letter-spacing: 0.4px; white-space: nowrap;
  }
  .hours {
    position: absolute; left: 220px; top: 127px; color: var(--text);
    font-size: 17.5px; line-height: 19.8px; letter-spacing: 0.3px; white-space: nowrap;
  }
  .hours__title { font-weight: 600; letter-spacing: 0.6px; }
  .contact { position: absolute; left: 219px; top: 250px; list-style: none; }
  .contact li {
    display: flex; align-items: center; gap: 11px; height: 22.7px;
    font-size: 17.5px; letter-spacing: 0.6px; white-space: nowrap;
  }
  .contact svg { width: 15px; height: 16px; flex: none; }
</style>
</head>
<body>
<main class="sheet">

  <section class="card card--front" aria-label="Front of business card">
    <div class="pattern-zone pattern-zone--top" role="img" aria-label="Faint large outlined lettering pattern"></div>
    <div class="brand-band">
      <div class="brand">
        <p class="brand__name">FLUMO'S</p>
        <p class="brand__tagline">AUDIO &amp; VISUAL PRODUCTION</p>
      </div>
      <ul class="social">
        <li class="teal"><span class="mark"></span>@flumosproductions</li>
        <li class="cyan"><span class="mark"></span>@flumosproductions</li>
        <li class="purple"><span class="mark mark--round"></span>https://flumos.com.au</li>
      </ul>
    </div>
    <div class="pattern-zone pattern-zone--bottom" role="img" aria-label="Faint large outlined lettering pattern"></div>
  </section>

  <section class="card card--back" aria-label="Back of business card">
    <div class="pattern-column" role="img" aria-label="Faint large outlined lettering pattern"></div>
    <div class="back-head"><p class="brand__name">FLUMO'S</p></div>
    <p class="back-tagline">AUDIO &amp; VISUAL PRODUCTIONS</p>
    <div class="hours">
      <p class="hours__title">OPENING HOURS</p>
      <p>Mon–Fri: 7am–10pm</p>
      <p>Saturday: 8am–10pm</p>
      <p>Sunday: 8am–11pm</p>
    </div>
    <ul class="contact">
      <li class="teal">
        <svg viewBox="0 0 14 16" fill="currentColor"><path d="M3 1l2.5 3.2L4 6c.8 2.4 2.3 4.3 4.5 5.8l1.8-1.3L13 13l-1.6 2.2C6 14.5 1.5 8.5 1.2 2.5z"/></svg>
        0400 -555- 019</li>
      <li class="cyan">
        <svg viewBox="0 0 16 12" fill="currentColor"><path d="M0 0h16v1.5L8 7 0 1.5z"/><path d="M0 3.5l8 5.5 8-5.5V12H0z"/></svg>
        alex@flumos.com.au</li>
      <li class="purple">
        <svg viewBox="0 0 12 16" fill="currentColor"><path d="M6 0a6 6 0 0 1 6 6c0 4-6 10-6 10S0 10 0 6a6 6 0 0 1 6-6zm0 3.5a2.5 2.5 0 1 0 0 5 2.5 2.5 0 0 0 0-5z"/></svg>
        Harbour Bay, Queensland Australia</li>
    </ul>
  </section>

</main>
</body>
</html>
```